Self-Help Book Cover

This is a self-help book entitled, "Lanterns for Loners, Oddballs & Dreamers: A grounded and soulful guide to finding your footing among others."
I want the book cover to be primarily white, with red and black as secondary colors. I am open to cartoon interpretations of the words, "misfits, weirdos, and introverts" or a unique font used for each word. For the center, there can be white/gray people/balls with larger red people/balls in the middle of them shaped like an antique key. Or the center can be a red door that opens to a pleasant background image (maybe nature). This is just some ideas, I am open to others.
The author's name is Rosalind Whitcombe. The text on the back of the book is in a word doc file attached. I have also attached samples of the key and people/balls.
Updates
Requirements
Must have
- a .jpg or .tif(f) file
- at least 1000 pixels on the longest side
- ideal image height/width ratio is 1.6 (example: 1000 x 1600)
- The size should be 5.5" x 8.5"

```html
<!DOCTYPE html>
<html lang="en">
<head>
<meta charset="utf-8">
<title>Lanterns for Loners, Oddballs &amp; Dreamers — Book Cover</title>
<link rel="stylesheet" href="https://fonts.googleapis.com/css2?family=Oswald:wght@500;700&family=Roboto:wght@300;400&family=Dancing+Script:wght@500&display=swap">
<style>
  :root {
    --page-bg: #ffffff;
    --cover-top: #c9c9c9;
    --cover-mid: #e4e4e4;
    --cover-bottom: #ffffff;
    --ink: #111111;
    --accent-red: #e3262b;
    --rule: #8a8a8a;
    --crowd-light: #f4f4f4;
    --crowd-mid: #d2d2d2;
  }
  html, body {
    margin: 0;
    padding: 0;
    width: 1200px;
    height: 1200px;
    overflow: hidden;
    background: var(--page-bg);
  }
  .canvas {
    position: relative;
    width: 1200px;
    height: 1200px;
  }
  .cover {
    position: absolute;
    left: 250px;
    top: 59px;
    width: 700px;
    height: 1082px;
    overflow: hidden;
    background: linear-gradient(to bottom, var(--cover-top) 0%, var(--cover-mid) 40%, var(--cover-bottom) 85%);
    box-shadow: 0 6px 24px rgba(0,0,0,0.18);
  }
  .title {
    position: absolute;
    left: 0;
    top: 110px;
    width: 100%;
    text-align: center;
    margin: 0;
  }
  .title-main {
    display: block;
    font-family: 'Oswald', sans-serif;
    font-weight: 700;
    font-size: 132px;
    line-height: 1;
    letter-spacing: 1px;
    color: var(--ink);
    text-transform: uppercase;
  }
  .title-main .red { color: var(--accent-red); }
  .title-for {
    position: absolute;
    left: 290px;
    top: 112px;
    font-family: 'Dancing Script', cursive;
    font-weight: 500;
    font-size: 84px;
    color: #ffffff;
    line-height: 1;
  }
  .title-sub {
    display: block;
    margin-top: 40px;
    font-family: 'Roboto', sans-serif;
    font-weight: 300;
    font-size: 58px;
    line-height: 1.08;
    color: var(--ink);
    text-transform: uppercase;
  }
  .crowd {
    position: absolute;
    left: 0;
    top: 430px;
    width: 700px;
    height: 420px;
    background:
      radial-gradient(ellipse 60px 80px at 50% 48%, var(--accent-red) 0 55%, transparent 75%),
      radial-gradient(ellipse closest-side at 50% 50%, var(--crowd-light) 0%, var(--crowd-mid) 55%, rgba(210,210,210,0) 100%);
  }
  .subtitle {
    position: absolute;
    left: 60px;
    width: 580px;
    top: 830px;
    text-align: center;
    font-family: 'Roboto', sans-serif;
    font-weight: 400;
    font-size: 22px;
    line-height: 1.3;
    letter-spacing: 0.5px;
    color: var(--ink);
    text-transform: uppercase;
    border-top: 1px solid var(--rule);
    border-bottom: 1px solid var(--rule);
    padding: 10px 0;
    margin: 0;
  }
  .author {
    position: absolute;
    left: 0;
    width: 100%;
    top: 955px;
    text-align: center;
    white-space: nowrap;
    font-family: 'Oswald', sans-serif;
    font-weight: 500;
    font-size: 44px;
    line-height: 1.2;
    letter-spacing: 8px;
    color: var(--ink);
    text-transform: uppercase;
    margin: 0;
  }
</style>
</head>
<body>
<div class="canvas">
  <div class="cover">
    <h1 class="title">
      <span class="title-main">Lan<span class="red">terns</span></span>
      <span class="title-for">for</span>
      <span class="title-sub">Loners, Oddballs &amp;<br>Dreamers</span>
    </h1>
    <div class="crowd" role="img" aria-label="A soft-focus crowd of white figures with a single red figure standing in the middle"></div>
    <p class="subtitle">A grounded and soulful guide<br>to finding your footing among others</p>
    <p class="author">Rosalind Whitcombe</p>
  </div>
</div>
</body>
</html>
```